Brisco Beverage Co.

Brisco is a new beverage company that currently specializes in energy and hydration. I need label design for the bottles. The label will be a full sleeve so free free to use the entire bottle. The premise behind the product is that its a Brisco from the competition. The label needs to say smart, strong, expensive. The background for the label will be black.
Updates

I need an entire label design as well as logo

Target Market(s)

20-30 year old active people.

Industry/Entity Type

It Company

Logo Text

By athletes for the athlete in all of us.

Logo styles of interest
Pictorial/Combination Logo
Wordmark Logo
Requirements
Must have
• the flavors are fruit based. Blackberry lime, mango pineapple, mango berry, strawberry kiwi. Incorporate natural looking fruit into the design.

```html
<!DOCTYPE html>
<html lang="en">
<head>
<meta charset="utf-8">
<title>Brisco — Natural Hydration Drink Labels</title>
<link rel="stylesheet" href="https://fonts.googleapis.com/css2?family=Montserrat:wght@600;800;900&display=swap">
<style>
  :root {
    --bg: #000000;
    --label: #1a1a1a;
    --label-edge: #2a2a2a;
    --white: #ffffff;
    --muted: #9a9a9a;
    --logo-yellow: #f3dc3c;
    --apple-plum: #ec5a2a;
    --mango-pineapple: #f0d23a;
    --blackberry-lime: #8e3a9e;
    --strawberry-kiwi: #e8383a;
    --tag-apple-plum: #c8491f;
    --tag-mango-pineapple: #e8c52a;
    --tag-blackberry-lime: #6d2a78;
    --tag-strawberry-kiwi: #c8202a;
  }
  * { box-sizing: border-box; margin: 0; padding: 0; }
  html, body {
    width: 1200px; height: 900px; overflow: hidden;
    background: var(--bg);
    font-family: "Montserrat", sans-serif;
    color: var(--white);
  }
  .canvas { position: relative; width: 1200px; height: 900px; }

  .brand-mark {
    position: absolute; top: 78px; left: 0; width: 1200px;
    text-align: center;
    font-weight: 900; font-size: 92px; letter-spacing: 2px;
    color: var(--logo-yellow);
    line-height: 1;
  }

  .label {
    position: absolute; top: 240px; width: 180px; height: 570px;
    background: var(--label);
    border: 1px solid var(--label-edge);
    border-radius: 26px;
    display: flex; flex-direction: column; align-items: center;
  }
  .label--apple-plum { left: 130px; }
  .label--mango-pineapple { left: 375px; }
  .label--blackberry-lime { left: 620px; }
  .label--strawberry-kiwi { left: 866px; }

  .label__tagline {
    margin-top: 66px;
    font-weight: 800; font-size: 9.5px; line-height: 1.15;
    text-align: center; text-transform: uppercase;
  }
  .label__fruit {
    margin-top: 10px; width: 150px; height: 370px;
    border-radius: 40px;
    position: relative;
  }
  .label--apple-plum .label__fruit { background: radial-gradient(ellipse at 50% 50%, #6a2a3a 0%, #8fb04a 40%, #3a1420 75%, transparent 100%); }
  .label--mango-pineapple .label__fruit { background: radial-gradient(ellipse at 50% 50%, #e8b030 0%, #9aa03a 45%, #6a5a1a 75%, transparent 100%); }
  .label--blackberry-lime .label__fruit { background: radial-gradient(ellipse at 50% 50%, #8ccf3a 0%, #3a2a4a 50%, #1e1a28 78%, transparent 100%); }
  .label--strawberry-kiwi .label__fruit { background: radial-gradient(ellipse at 50% 50%, #9ab83a 0%, #c82a2a 50%, #5a2a1a 78%, transparent 100%); }

  .label__name {
    position: absolute; top: 150px; left: -10px; width: 170px;
    text-align: center; font-weight: 900; font-size: 38px; letter-spacing: 1px;
  }
  .label--apple-plum .label__name { color: var(--apple-plum); }
  .label--mango-pineapple .label__name { color: var(--mango-pineapple); }
  .label--blackberry-lime .label__name { color: var(--blackberry-lime); }
  .label--strawberry-kiwi .label__name { color: var(--strawberry-kiwi); }

  .label__flavours {
    position: absolute; top: 205px; left: -15px; width: 180px;
    display: flex; justify-content: space-between;
  }
  .flavour-tag {
    font-weight: 800; font-size: 9.5px; text-transform: uppercase;
    padding: 4px 5px; color: var(--white);
  }
  .label--apple-plum .flavour-tag { background: var(--tag-apple-plum); }
  .label--mango-pineapple .flavour-tag { background: var(--tag-mango-pineapple); color: #111; }
  .label--blackberry-lime .flavour-tag { background: var(--tag-blackberry-lime); }
  .label--strawberry-kiwi .flavour-tag { background: var(--tag-strawberry-kiwi); }

  .label__descriptor {
    margin-top: 8px;
    font-weight: 800; font-size: 11px; text-transform: uppercase; white-space: nowrap;
  }
  .label--apple-plum .hl { color: var(--apple-plum); }
  .label--mango-pineapple .hl { color: var(--mango-pineapple); }
  .label--blackberry-lime .hl { color: #c43ad0; }
  .label--strawberry-kiwi .hl { color: var(--strawberry-kiwi); }

  .label__fine {
    width: 150px; display: flex; justify-content: space-between;
    font-weight: 600; font-size: 5px; color: var(--muted); margin-top: 3px;
  }
  .label__volume { font-weight: 600; font-size: 8px; color: var(--muted); margin-top: 1px; }
  .label__swatch { width: 30px; height: 26px; margin-top: 14px; border-radius: 3px; }
  .label--apple-plum .label__swatch { background: var(--tag-apple-plum); }
  .label--mango-pineapple .label__swatch { background: var(--tag-mango-pineapple); }
  .label--blackberry-lime .label__swatch { background: #9a2aa8; }
  .label--strawberry-kiwi .label__swatch { background: var(--tag-strawberry-kiwi); }
</style>
</head>
<body>
<main class="canvas">
  <div class="brand-mark">BRISCO</div>

  <section class="label label--apple-plum">
    <p class="label__tagline">Brisco<br>from the<br>competition</p>
    <div class="label__fruit" role="img" aria-label="Photographic arrangement of plums, cherries and green apples">
      <div class="label__name">BRISCO</div>
      <div class="label__flavours"><span class="flavour-tag">Apple</span><span class="flavour-tag">Plum</span></div>
    </div>
    <p class="label__descriptor">Natural <span class="hl">Hydration</span> Drink</p>
    <div class="label__fine"><span>made from concentrate</span><span>fait de concentré</span></div>
    <p class="label__volume">500 mL (17.6 fl oz)</p>
    <div class="label__swatch"></div>
  </section>

  <section class="label label--mango-pineapple">
    <p class="label__tagline">Brisco<br>from the<br>competition</p>
    <div class="label__fruit" role="img" aria-label="Photographic arrangement of mangoes and pineapples">
      <div class="label__name">BRISCO</div>
      <div class="label__flavours"><span class="flavour-tag">Mango</span><span class="flavour-tag">Pineapple</span></div>
    </div>
    <p class="label__descriptor">Natural <span class="hl">Hydration</span> Drink</p>
    <div class="label__fine"><span>made from concentrate</span><span>fait de concentré</span></div>
    <p class="label__volume">500 mL (17.6 fl oz)</p>
    <div class="label__swatch"></div>
  </section>

  <section class="label label--blackberry-lime">
    <p class="label__tagline">Brisco<br>from the<br>competition</p>
    <div class="label__fruit" role="img" aria-label="Photographic arrangement of blackberries and lime slices">
      <div class="label__name">BRISCO</div>
      <div class="label__flavours"><span class="flavour-tag">Blackberry</span><span class="flavour-tag">Lime</span></div>
    </div>
    <p class="label__descriptor">Natural <span class="hl">Hydration</span> Drink</p>
    <div class="label__fine"><span>made from concentrate</span><span>fait de concentré</span></div>
    <p class="label__volume">500 mL (17.6 fl oz)</p>
    <div class="label__swatch"></div>
  </section>

  <section class="label label--strawberry-kiwi">
    <p class="label__tagline">Brisco<br>from the<br>competition</p>
    <div class="label__fruit" role="img" aria-label="Photographic arrangement of strawberries and kiwi halves">
      <div class="label__name">BRISCO</div>
      <div class="label__flavours"><span class="flavour-tag">Strawberry</span><span class="flavour-tag">Kiwi</span></div>
    </div>
    <p class="label__descriptor">Natural <span class="hl">Hydration</span> Drink</p>
    <div class="label__fine"><span>made from concentrate</span><span>fait de concentré</span></div>
    <p class="label__volume">500 mL (17.6 fl oz)</p>
    <div class="label__swatch"></div>
  </section>
</main>
</body>
</html>
```